Website Design for a chemical distribution company

Designer must provide full implementation/coding depending on the platform chosen by the client we'd prefer wordpress type CMS system.

We need a modern and bold website setup for our chemical distribution company. It will need to be like a web store however, no purchases take place on the website only inquiries. So for example the customer can go to a product and click on a button that brings up an inquiry window, they populate that with their information and it sends me an email with the inquiry.

We need it done 3 times pretty much the same but maybe a different colour scheme for each industry. for example on the welcome screen we want 3 icons /pictures ie: plastic, resin, industrial. When the customer clicks on the industry they need it directs them to the specific area that is perhaps on a subdomain or somewhere on the main domain but with no relation to the other industries I hope this makes sense. The layout would be the same but their should be some difference such as colours etc.

The site needs to have a powerful search engine that is very accurate.

It will have about 40,000 products and needs to be able to upload our products via an excel spreed sheet.

We need it to look graphically amazing and very easy to use for the customer.

It will also need to have a blog section that we can upload blogs to daily with different sub categories for things such as experiments, news etc.

The front page needs to be have a banner/advertisement window that is easy for us to change with new specials/deals that we bring out.

Basically the site needs to be easy to navigate, easy to get to products and inquire and needs to have a wow factor.

We also need a special requess page that gives the customers the facility to request a product that they can't find on our website.

I need to stress the importance of a search engine on the site that can handle searching through all the products.

We will also give you the words and you will need to put those on to the pages.

You will also be required to upload our catalogue via CSV or Excel to the site on final completion.

Please find similar websites below for companies that similar to us:

www.tarvelo.com
www.brenti-koval.com
http://www.northumlab.com.au

Just to clarify only one of the websites will have 40-50k products the other 2 industries will only have about 200-500 products each. Added Sunday, February 14, 2016

Reason: Finalising designs and need more time.

Target Market(s)

Chemicals, Food, Pharmaceuticals, Business to Business

Industry/Entity Type

It Company

Coding

Coded - Design and coding required

Number of Pages Required

5+ page

Font styles to use
Sans Serif

Requirements
Must have
• Powerful search engine
• Great design
• Easy to use CMS
• SEO
• Mobile Device Compatible

```html
<!DOCTYPE html>
<html lang="en">
<head>
<meta charset="utf-8">
<title>Nuvora — Specialty Ingredient Supplier</title>
<link rel="stylesheet" href="https://fonts.googleapis.com/css2?family=Open+Sans:wght@400;600;700&family=Roboto:wght@300;400;500;700&family=Lora:wght@400&display=swap">
<style>
:root{
  --blue:#0a6fc2;
  --blue-dark:#085a9e;
  --ink:#2b2b2b;
  --muted:#6d6d6d;
  --dark:#141414;
  --footer:#232323;
  --white:#ffffff;
  --red:#d82a2a;
  --hero-bg:#e9eef3;
}
*{box-sizing:border-box;margin:0;padding:0}
html,body{width:1200px;height:2314px;overflow:hidden}
body{position:relative;background:var(--white);font-family:"Open Sans",Arial,sans-serif;color:var(--ink)}
.abs{position:absolute}

/* header */
.header{position:absolute;left:0;top:0;width:1200px;height:136px;background:var(--white)}
.social{position:absolute;display:flex;gap:9px}
.social span{width:30px;height:30px;border-radius:50%;border:2px solid #b9b9b9;display:block}
.social span.on{background:#1c7cd0;border-color:#1c7cd0}
.brand{position:absolute;left:600px;top:65px;transform:translate(-50%,-50%);display:flex;align-items:center;gap:12px;font-family:"Roboto",sans-serif;font-weight:500;font-size:56px;color:var(--blue);letter-spacing:1px}
.brand i{width:18px;height:18px;border-radius:50%;background:var(--blue);display:block}
.header-tools{position:absolute;right:30px;top:18px;display:flex;gap:22px}
.header-contact{position:absolute;right:30px;top:84px;font-size:16px;color:#444}
.header-contact b{font-family:"Roboto",sans-serif;font-weight:500;font-size:24px;color:var(--blue);margin-left:8px;vertical-align:-2px}

/* nav */
.nav{position:absolute;left:0;top:136px;width:1200px;height:54px;background:var(--blue);border-bottom:3px solid #cfe0ef}
.nav a{position:absolute;top:0;height:51px;line-height:51px;color:var(--white);font-family:"Open Sans",sans-serif;font-weight:700;font-size:16px;text-decoration:none}
.nav a.active{left:26px;top:4px;height:44px;line-height:44px;width:100px;text-align:center;background:var(--white);color:var(--blue)}
.search{position:absolute;left:930px;top:4px;width:239px;height:45px;background:var(--white);border:2px solid var(--white)}
.search span{position:absolute;left:14px;top:10px;color:#9a9a9a;font-size:17px}
.search i{position:absolute;right:0;top:0;width:43px;height:41px;background:var(--blue)}

/* hero */
.hero{position:absolute;left:0;top:191px;width:1200px;height:520px;background:linear-gradient(90deg,#f2f4f6 0%,#e6ebf0 55%,#dfe6ec 100%)}
.hero-art{position:absolute;left:676px;top:216px;width:524px;height:465px;background:radial-gradient(ellipse at 55% 55%,#cfd9e2 0%,#e2e8ee 70%,rgba(226,232,238,0) 100%)}
.hero h1{position:absolute;left:26px;top:245px;font-family:"Roboto",sans-serif;font-weight:300;font-size:54px;line-height:71px;color:#333;text-transform:uppercase}
.hero h1 b{font-weight:700;color:var(--blue)}
.hero-sub{position:absolute;left:26px;top:413px;font-family:"Roboto",sans-serif;font-weight:500;font-size:24px;color:var(--blue)}
.hero-text{position:absolute;left:26px;top:466px;width:620px;font-size:18px;line-height:30px;color:#444}
.btn{position:absolute;background:var(--blue);color:var(--white);font-weight:600;font-size:16px;text-align:center}

/* segments */
.section-title{position:absolute;left:26px;font-family:"Roboto",sans-serif;font-weight:500;font-size:27px;text-transform:uppercase}
.section-sub{position:absolute;left:26px;font-size:16px}
.card{position:absolute;top:800px;width:361px;height:360px;background:var(--white);border:2px solid var(--white)}
.card .pic{height:180px;border-bottom:2px solid var(--blue)}
.card .badge{position:absolute;left:140px;top:130px;width:80px;height:80px;background:var(--blue);border:3px solid var(--white)}
.card .badge svg{position:absolute;left:20px;top:20px}
.card h3{position:absolute;top:224px;width:100%;text-align:center;font-family:"Roboto",sans-serif;font-weight:500;font-size:24px;color:var(--blue)}
.card p{position:absolute;top:272px;left:20px;right:20px;text-align:center;font-size:16px;line-height:28px;color:#888}

/* blog */
.post{position:absolute;top:1367px;width:361px}
.post .pic{height:169px}
.date{position:absolute;left:0;top:180px;width:59px;height:69px;border:2px solid #8a8a8a;color:#bbb;text-align:center}
.date b{display:block;font-weight:400;font-size:21px;line-height:38px}
.date span{display:block;border-top:2px solid #8a8a8a;font-size:13px;line-height:25px}
.post p{position:absolute;left:78px;top:196px;width:280px;font-size:16px;line-height:26px;color:#9a9a9a}
.post.featured .date{border-color:var(--blue);color:var(--blue)}
.post.featured .date span{border-color:var(--blue)}
.post.featured p{color:#2f8fe0}

/* promo */
.promo{position:absolute;left:25px;top:1718px;width:1144px;height:284px;border:12px solid #d9d9d9;background:#e4e8eb}
.promo h2{position:absolute;left:60px;top:28px;font-family:"Roboto",sans-serif;font-weight:500;font-size:42px;color:var(--red)}
.promo .label{position:absolute;top:95px;font-family:"Lora",serif;font-size:21px}
.promo .thumb{position:absolute;top:118px;height:112px;width:150px;border-radius:10px}
.promo-photo{position:absolute;left:680px;top:0;width:452px;height:260px;background:linear-gradient(120deg,#cfd8e0,#9fb1c2 60%,#7d8e9e);clip-path:polygon(80px 0,100% 0,100% 100%,0 100%)}
.promo-stripe{position:absolute;left:660px;top:0;width:30px;height:260px;background:#e85a1e;clip-path:polygon(70px 0,86px 0,16px 100%,0 100%)}
.buy{position:absolute;left:1004px;top:213px;width:106px;height:38px;border:2px solid var(--white);color:var(--white);font-size:16px;line-height:34px;text-align:center;background:rgba(0,0,0,.25)}

/* footer */
.footer{position:absolute;left:0;top:2053px;width:1200px;height:261px;background:var(--footer);color:#c8c8c8}
.footer-links{position:absolute;left:0;top:24px;width:1200px;text-align:center;font-size:15px;color:#b5b5b5}
.footer-links b{color:var(--white);font-weight:400}
.footer-links i{font-style:normal;margin:0 12px;color:#888}
.footer-rule{position:absolute;left:26px;top:68px;width:1143px;height:1px;background:#444}
.footer h4{position:absolute;top:96px;font-size:17px;font-weight:600;color:#1e86dc;text-transform:uppercase}
.newsletter{position:absolute;left:26px;top:133px;width:358px;height:38px;border:1px solid #555;background:#1c1c1c}
.newsletter span{position:absolute;left:12px;top:8px;font-size:16px;color:#ddd}
.newsletter i{position:absolute;right:-1px;top:-1px;width:48px;height:38px;background:var(--blue)}
.contact-line{position:absolute;left:532px;width:306px;height:38px;border-bottom:1px solid #3d3d3d;font-size:14px;color:#ddd;padding-left:26px;line-height:38px}
.contact-line svg{position:absolute;left:2px;top:11px}
.footer-brand{position:absolute;left:990px;top:125px;font-family:"Roboto",sans-serif;font-weight:500;font-size:46px;color:#8d8d8d}
.copy{position:absolute;left:982px;top:193px;font-size:13px;line-height:22px;color:#bbb}
</style>
</head>
<body>

<header class="header">
  <div class="social" style="left:26px;top:51px"><span class="on"></span><span></span><span></span><span></span><span></span><span></span></div>
  <div class="brand"><i></i>Nuvora</div>
  <div class="header-tools">
    <svg width="36" height="40" viewBox="0 0 36 40"><circle cx="16" cy="11" r="9" fill="#0a6fc2"/><path d="M2 38c0-10 6-16 14-16s14 6 14 16z" fill="#0a6fc2"/><circle cx="28" cy="30" r="7" fill="#fff" stroke="#0a6fc2" stroke-width="2"/><path d="M28 26v8M24 30h8" stroke="#0a6fc2" stroke-width="2"/></svg>
    <svg width="42" height="40" viewBox="0 0 42 40"><path d="M2 6h7l6 22h20l4-15H12" fill="none" stroke="#555" stroke-width="3"/><circle cx="17" cy="35" r="3" fill="#555"/><circle cx="32" cy="35" r="3" fill="#555"/><path d="M34 1v10M29 6h10" stroke="#555" stroke-width="2.5"/></svg>
  </div>
  <div class="header-contact">Contact the Nuvora <b>123 456 7890</b></div>
</header>

<nav class="nav">
  <a class="active" href="#">HOME</a>
  <a href="#" style="left:162px">ABOUT</a>
  <a href="#" style="left:281px">MARKET SEGMENTS</a>
  <a href="#" style="left:498px">PRODUCT</a>
  <a href="#" style="left:637px">BLOG</a>
  <a href="#" style="left:745px">CONTACT</a>
  <div class="search"><span>Search...</span><i><svg width="43" height="41" viewBox="0 0 43 41"><circle cx="24" cy="18" r="8" fill="none" stroke="#fff" stroke-width="2.5"/><path d="M18 24l-7 7" stroke="#fff" stroke-width="3"/></svg></i></div>
</nav>

<section class="hero">
</section>
<div class="hero-art" role="img" aria-label="Laboratory glassware illustration: flasks on a stand, a scale and a rack of coloured test tubes"></div>
<h1 class="hero" style="background:none;height:auto;width:auto;top:0;left:0"></h1>
<h1 class="abs" style="left:26px;top:245px;font-family:'Roboto',sans-serif;font-weight:300;font-size:54px;line-height:71px;color:#333">THE <b style="font-weight:700;color:var(--blue)">GO TO</b> SPECIALTY<br>INGREDIENT SUPPLIER</h1>
<p class="hero-sub">FOR FLAVOR, PLASTIC, RESIN, INDUSTRIAL AND MORE</p>
<p class="hero-text">Chemical Distribution for simplicity makes things easy for YOU; offering quick turn-around, premium customer service, and 40,000 products!</p>
<div class="btn" style="left:26px;top:565px;width:134px;height:44px;line-height:44px">READ MORE</div>

<svg class="abs" style="left:0;top:655px" width="1200" height="600" viewBox="0 0 1200 600">
  <polygon points="0,5 1200,57 1200,600 0,600" fill="#0a6fc2"/>
  <polygon points="0,597 1200,533 1200,600" fill="#141414"/>
</svg>
<div class="abs" style="left:0;top:1188px;width:1200px;height:490px;background:linear-gradient(180deg,#1c1f22,#111)"></div>
<svg class="abs" style="left:0;top:1188px" width="1200" height="66" viewBox="0 0 1200 66"><polygon points="0,0 1200,0 0,64" fill="#0a6fc2"/></svg>

<h2 class="section-title" style="top:708px;color:#fff">The Chemical Distribution Company</h2>
<p class="section-sub" style="top:752px;color:#e3eefa">Customers love Tarvelo because they're assured materials will be received on time and on specification, taking the stress out of their daily routines.</p>

<article class="card" style="left:26px">
  <div class="pic" role="img" aria-label="Photo of a person holding a plastic water bottle" style="background:linear-gradient(90deg,#f0b9c4,#f6d6d6 60%,#e9c0bd)"></div>
  <div class="badge"><svg width="40" height="40" viewBox="0 0 40 40"><path d="M16 2h8v6l4 4v26H12V12l4-4z" fill="none" stroke="#fff" stroke-width="2.5"/><path d="M12 20h16" stroke="#fff" stroke-width="2"/></svg></div>
  <h3>PLASTIC</h3>
  <p>Lorem ipsum dolor sit amet, consectetur dolar sitadipiscing elitroin cursus</p>
</article>
<article class="card" style="left:418px">
  <div class="pic" role="img" aria-label="Photo of coloured plastic sheets and bowls of resin pellets" style="background:linear-gradient(90deg,#3bc6a0,#6fc25a 40%,#d3c6a6 70%,#e27aa4)"></div>
  <div class="badge"><svg width="40" height="40" viewBox="0 0 40 40"><path d="M20 3l15 8v18l-15 8-15-8V11z M5 11l15 8 15-8 M20 19v18" fill="none" stroke="#fff" stroke-width="2.5"/></svg></div>
  <h3>RESIN</h3>
  <p>Lorem ipsum dolor sit amet, consectetur dolar sitadipiscing elitroin cursus</p>
</article>
<article class="card" style="left:810px">
  <div class="pic" role="img" aria-label="Photo of industrial pipework and valves" style="background:linear-gradient(90deg,#8f9aa4,#c3c9ce 45%,#b46a5a 80%,#8a8f95)"></div>
  <div class="badge"><svg width="40" height="40" viewBox="0 0 40 40"><path d="M3 37V18l9 6v-6l9 6v-6l9 6V6h6v31z" fill="#fff"/></svg></div>
  <h3>INDUSTRIAL</h3>
  <p>Lorem ipsum dolor sit amet, consectetur dolar sitadipiscing elitroin cursus</p>
</article>

<h2 class="section-title" style="top:1275px;color:#1e86dc">Latest Blog</h2>
<p class="section-sub" style="top:1319px;color:#8c8c8c">Customers love Tarvelo because they're assured materials will be received on time and on specification, taking the stress out of their daily routines.</p>

<article class="post featured" style="left:26px">
  <div class="pic" role="img" aria-label="Photo of a business team meeting around a laptop" style="background:linear-gradient(90deg,#6b7a8c,#c8cdd4 50%,#556170)"></div>
  <div class="date"><b>29</b><span>Feb</span></div>
  <p>Lorem ipsum dolor sit amet, consect etur adipiscing eli</p>
</article>
<article class="post" style="left:418px">
  <div class="pic" role="img" aria-label="Black and white photo of hands writing at a desk" style="background:linear-gradient(90deg,#d4d4d4,#f2f2f2 50%,#9a9a9a)"></div>
  <div class="date"><b>29</b><span>Feb</span></div>
  <p>Lorem ipsum dolor sit amet consecte tur adipiscing eli</p>
</article>
<article class="post" style="left:810px">
  <div class="pic" role="img" aria-label="Black and white photo of people reviewing documents" style="background:linear-gradient(90deg,#8a8a8a,#ededed 55%,#b0b0b0)"></div>
  <div class="date"><b>29</b><span>Feb</span></div>
  <p>Lorem ipsum dolor sit amet consecte tur adipiscing eli</p>
</article>

<section class="promo">
  <h2>Speciality Chemical Products</h2>
  <p class="label" style="left:32px;color:#1e3e78">Plastic Product</p>
  <p class="label" style="left:265px;color:#14402a">Resin Product</p>
  <p class="label" style="left:485px;color:#1f3ee0">Industrial Product</p>
  <div class="thumb" role="img" aria-label="Coloured plastic buckets" style="left:42px;background:linear-gradient(90deg,#35b8d8,#e05848)"></div>
  <div class="thumb" role="img" aria-label="Piles of resin granules" style="left:238px;width:180px;background:linear-gradient(90deg,#c24a3a,#3a3a3a 50%,#c8962e)"></div>
  <div class="thumb" role="img" aria-label="Coloured plastic rods and tubes" style="left:482px;background:linear-gradient(90deg,#e2473a,#2e4fa8 60%,#e5c02d)"></div>
  <div class="promo-stripe"></div>
  <div class="promo-photo" role="img" aria-label="Photo of a lab scientist using a pipette"></div>
  <div class="buy">BUY NOW</div>
</section>

<footer class="footer">
  <p class="footer-links"><b>Home</b><i>/</i>About<i>/</i>Principals<i>/</i>Market Segments<i>/</i>Product<i>/</i>Blog<i>/</i>Contact</p>
  <div class="footer-rule"></div>
  <h4 style="left:26px">Subscribe to our newsletter</h4>
  <div class="newsletter"><span>@email_address</span><i><svg width="48" height="38" viewBox="0 0 48 38"><path d="M14 19l22-9-6 20-5-7z" fill="#fff"/></svg></i></div>
  <div class="social" style="left:26px;top:198px"><span class="on"></span><span></span><span></span><span></span><span></span><span></span></div>
  <h4 style="left:532px">Contact</h4>
  <div class="contact-line" style="top:128px"><svg width="14" height="16" viewBox="0 0 14 16"><circle cx="7" cy="5" r="4" fill="none" stroke="#1e86dc" stroke-width="2"/><path d="M7 9v7" stroke="#1e86dc" stroke-width="2"/></svg>24 Orchard Lane, Springvale</div>
  <div class="contact-line" style="top:166px"><svg width="14" height="16" viewBox="0 0 14 16"><path d="M2 2l3-1 2 4-2 2c1 2 2 3 4 4l2-2 4 2-1 3c-6 0-12-6-12-12z" fill="#1e86dc"/></svg>123.456.7890</div>
  <div class="contact-line" style="top:204px;border:none"><svg width="16" height="14" viewBox="0 0 16 14"><rect x="1" y="2" width="14" height="10" fill="none" stroke="#1e86dc" stroke-width="2"/><path d="M1 2l7 6 7-6" fill="none" stroke="#1e86dc" stroke-width="1.5"/></svg>info@nuvorachem.com</div>
  <div class="footer-brand">Nuvora</div>
  <p class="copy">© 2016 Chemical Distribtation.<br>All Rights Reserved.</p>
</footer>

</body>
</html>
```